Jewelry Manufacturing & Repair business needs advertising mailout - 9x4 flyer

Need new double sided flyer designed for an insert into a mailout. Want 9x4 (vertical design) to fit in 9.5" x 4.125" envelopes. Company based out of Louisiana called "Lem Travis Manufacturing." Been in business for 45 years. We specialize in custom jewelry design and casting on the wholesale level. We are a full service trade shop offering CAD design, casting services, basic and advanced jewelry repair. Most of our customers are drawn to the fact that they talk directly with the owner/designer of the company each time they call. I've attached several images of CAD renders we've built and of our logo. I've also attached a copy of an old mailout we sent out 10 years ago that I designed myself (and it needed a lot of work). The business information listed in this old mailout is correct, except that we’ve been in business 45 years now. I would like the final design to be "business bold," portraying business strength and stability. I like shades of blue, or a gold/silver color scheme. Logo is black and white. Need double sided.

Looking for project to be less wordy than the 10 yr old mailout. Don’t need the “example scenario” in this flyer.
Updates

The weekend has made the 2 day timeframe very tight. Would like to extend timeframe, but I will select a design on Monday at 3:00 pm (USA Central time).

Target Market(s)

Retail Jewelry Stores

Industry/Entity Type

Jewelry

Colors
cfdeed
0455a3
3176b5
85acd3

Requirements
Must have
• All contact information.
Nice to have
• Purpose of this flyer is to get new accounts for our business. We want something that the retail jewelry store will notice something that will make them not throw away immediately, but instead hold onto for the future.
• This upcoming Christmas season is usually very busy for retail stores, so we can help take some of the overflow of work and still meet deadlines. With our help, they shouldn't have to turn any customer away.
Should not have
• We will be partnering in this mailout with a sister wholesale diamond company. Therefore, we don't want to mention that our company sells any diamonds, as we want to leave that part up to our sister company.

```html
<!DOCTYPE html>
<html lang="en">
<head>
<meta charset="utf-8">
<title>Lem Travis Manufacturing – Mailout Flyer</title>
<link href="https://fonts.googleapis.com/css2?family=Raleway:wght@400;500;600;800&family=Patrick+Hand&display=swap" rel="stylesheet">
<style>
:root{
  --blue:#0455a3;
  --navy:#0a3470;
  --mid:#3176b5;
  --soft:#85acd3;
  --pale:#cfdeed;
  --ink:#1b1b1b;
  --white:#ffffff;
  --bg:#e9ecef;
}
*{box-sizing:border-box;margin:0;padding:0}
html,body{width:1200px;height:1200px;overflow:hidden;background:var(--bg)}
body{position:relative;font-family:"Raleway",Arial,sans-serif;color:var(--ink)}
.flyer{position:absolute;top:68px;width:500px;height:1064px;background:var(--white);overflow:hidden;box-shadow:0 6px 18px rgba(0,0,0,.18)}
.flyer--front{left:60px}
.flyer--back{left:640px;background:var(--pale)}

/* header */
.masthead{position:absolute;left:0;top:0;width:500px;height:153px;background:linear-gradient(180deg,var(--blue),#0a4f99)}
.brand-tag{position:absolute;left:32px;top:72px;display:flex;align-items:center;gap:8px;color:var(--white);font-size:15px;font-weight:600;letter-spacing:.5px}
.brand-tag__dot{width:16px;height:16px;border-radius:50%;border:2px solid var(--white);flex:none}
.masthead__name{position:absolute;left:170px;top:52px;color:var(--white);line-height:1}
.masthead__first{font-size:27px;font-weight:500;letter-spacing:.5px}
.masthead__second{font-size:32px;font-weight:800;margin-top:5px;letter-spacing:.3px}
.masthead__tag{font-size:8.6px;font-weight:500;margin-top:8px;letter-spacing:.1px}

/* front */
.hero{position:absolute;left:0;top:160px;width:500px;height:230px;background:linear-gradient(110deg,#e8e3de 0%,#f3eeea 45%,#c9b39a 75%,#8a6a4a 100%)}
.wave{position:absolute;left:0;top:300px}
.about{position:absolute;left:0;top:380px;width:500px;height:81px;background:var(--blue)}
.section-title{color:var(--white);line-height:1.05;border-left:3px solid var(--navy);padding-left:8px}
.section-title__light{font-size:16px;font-weight:500;display:block}
.section-title__bold{font-size:21px;font-weight:800;display:block}
.about .section-title{position:absolute;left:32px;top:12px;border-color:#0a2a5a}
.about__text{position:absolute;left:150px;top:10px;width:315px;color:var(--white);font-size:8.2px;line-height:1.5}
.offer{position:absolute;left:0;top:461px;width:500px;height:107px;background:var(--white)}
.offer__title{position:absolute;left:0;width:500px;top:13px;text-align:center;font-size:16px;font-weight:500}
.offer__title b{font-weight:800;color:var(--navy);border-bottom:2px solid var(--navy)}
.ticks{list-style:none;font-size:10.4px;line-height:15.5px}
.ticks li{display:flex;align-items:center;gap:6px}
.tick{flex:none}
.offer .ticks{position:absolute;top:44px}
.works{position:absolute;left:0;top:568px;width:500px;height:228px;background:var(--blue);color:var(--white)}
.works .section-title{position:absolute;left:30px;top:18px;border-color:var(--navy)}
.works__text{position:absolute;left:48px;top:72px;width:410px;font-size:8px;line-height:1.5}
.works__label{position:absolute;left:48px;top:118px;font-size:15px;font-variant:small-caps;letter-spacing:.5px}
.works .ticks{position:absolute;left:32px;top:137px;font-size:10.4px;line-height:15.6px}
.gallery{position:absolute;left:0;width:500px;display:flex;justify-content:space-around;padding:0 26px}
.gem{width:92px;height:92px;border-radius:50%;border:3px solid var(--blue)}
.gem--a{background:radial-gradient(circle at 45% 45%,#ffffff,#b9c0c8 55%,#5d6670)}
.gem--b{background:radial-gradient(circle at 50% 45%,#f4f1ea,#c7b185 55%,#6f5f45)}
.gem--c{background:radial-gradient(circle at 50% 50%,#d8cbb0,#8f8a7a 60%,#4a4a48)}
.gem--d{background:radial-gradient(circle at 45% 45%,#fbeee3,#d9a07a 55%,#8a4d2a)}
.call-bar{position:absolute;left:0;top:910px;width:500px;height:46px;background:var(--blue);color:var(--white);text-align:center;font-size:25px;font-weight:500;line-height:46px}
.sign-off{position:absolute;left:0;width:500px;text-align:center}
.sign-off__head{font-size:20px;font-weight:500;letter-spacing:.3px}
.sign-off__head b{font-weight:800}
.sign-off__firm{font-size:10.5px;font-weight:500;margin-top:2px}
.sign-off__firm small{font-size:8.5px}
.sign-off__contact{font-size:10.5px;font-weight:500;margin-top:14px}

/* back */
.intro{position:absolute;left:38px;top:176px;width:428px;font-size:10.2px;line-height:1.66}
.intro p+p{margin-top:9px}
.intro b{font-weight:600}
.voices-title{position:absolute;left:32px;top:378px;border-color:var(--blue);color:var(--blue)}
.voices-title .section-title__light{color:var(--ink);font-size:16px}
.voices-title .section-title__bold{color:var(--blue)}
.bubbles{position:absolute;left:215px;top:365px}
.quote{position:absolute;left:38px;width:428px;font-family:"Patrick Hand",cursive;font-size:12px;line-height:1.42;text-align:right}
.quote__by{font-family:"Raleway",sans-serif;font-size:10.2px;font-weight:500;color:var(--blue);text-align:right}
.back-call{position:absolute;left:0;top:920px;width:500px;text-align:center;font-size:25px;font-weight:500;line-height:30px}
.back-foot{position:absolute;left:0;top:955px;width:500px;height:109px;background:var(--blue);color:var(--white)}
</style>
</head>
<body>

<section class="flyer flyer--front" aria-label="Flyer front">
  <header class="masthead">
    <div class="brand-tag"><span class="brand-tag__dot"></span>LEM TRAVIS</div>
    <div class="masthead__name">
      <div class="masthead__first">LEM TRAVIS</div>
      <div class="masthead__second">MANUFACTURING</div>
      <div class="masthead__tag">TOP QUALITY CRAFTSMANSHIP, FRIENDLY PERSONAL SERVICE</div>
    </div>
  </header>

  <div class="hero" role="img" aria-label="Photo of a woman wearing an ornate gold drop earring"></div>
  <svg class="wave" width="500" height="90" viewBox="0 0 500 90" aria-hidden="true">
    <path d="M0 40 C120 0 260 10 500 85 L500 90 L0 90 Z" fill="#0a3470"/>
    <path d="M0 52 C130 10 270 20 500 90 L500 90 L0 90 Z" fill="#0455a3"/>
    <path d="M0 30 C130 -20 300 0 500 70 L500 52 C320 -10 140 -30 0 20 Z" fill="#ffffff"/>
  </svg>

  <div class="about">
    <h2 class="section-title"><span class="section-title__light">WHO WE</span><span class="section-title__bold">ARE?</span></h2>
    <p class="about__text">We are a family operated business, serving the jewelry industry for over <b>45 years.</b> Our experience provides us with a vast knowledge of the industry, as well as best practices for each unique item. We pride ourselves in quality craftsmanship with fast, honest, and courteous service.</p>
  </div>

  <div class="offer">
    <h2 class="offer__title">WHAT WE <b>OFFER?</b></h2>
    <ul class="ticks" style="left:32px">
      <li><svg class="tick" width="9" height="9" viewBox="0 0 10 10"><circle cx="5" cy="5" r="4.2" fill="none" stroke="#0455a3" stroke-width="1"/><path d="M3 5.2l1.5 1.4L7.4 3.6" fill="none" stroke="#0455a3" stroke-width="1.2"/></svg>Basic &amp; advanced jewelry repair</li>
      <li><svg class="tick" width="9" height="9" viewBox="0 0 10 10"><circle cx="5" cy="5" r="4.2" fill="none" stroke="#0455a3" stroke-width="1"/><path d="M3 5.2l1.5 1.4L7.4 3.6" fill="none" stroke="#0455a3" stroke-width="1.2"/></svg>Custom hand carved wax modeling</li>
      <li><svg class="tick" width="9" height="9" viewBox="0 0 10 10"><circle cx="5" cy="5" r="4.2" fill="none" stroke="#0455a3" stroke-width="1"/><path d="M3 5.2l1.5 1.4L7.4 3.6" fill="none" stroke="#0455a3" stroke-width="1.2"/></svg>CAD / CAM services for intricate detail</li>
    </ul>
    <ul class="ticks" style="left:302px">
      <li><svg class="tick" width="9" height="9" viewBox="0 0 10 10"><circle cx="5" cy="5" r="4.2" fill="none" stroke="#0455a3" stroke-width="1"/><path d="M3 5.2l1.5 1.4L7.4 3.6" fill="none" stroke="#0455a3" stroke-width="1.2"/></svg>Gold &amp; Platinum casting</li>
      <li><svg class="tick" width="9" height="9" viewBox="0 0 10 10"><circle cx="5" cy="5" r="4.2" fill="none" stroke="#0455a3" stroke-width="1"/><path d="M3 5.2l1.5 1.4L7.4 3.6" fill="none" stroke="#0455a3" stroke-width="1.2"/></svg>Furnish waxes, raw castings,</li>
      <li><svg class="tick" width="9" height="9" viewBox="0 0 10 10"><circle cx="5" cy="5" r="4.2" fill="none" stroke="#0455a3" stroke-width="1"/><path d="M3 5.2l1.5 1.4L7.4 3.6" fill="none" stroke="#0455a3" stroke-width="1.2"/></svg>or finished products</li>
    </ul>
  </div>

  <div class="works">
    <h2 class="section-title"><span class="section-title__light">HOW IT</span><span class="section-title__bold">WORKS?</span></h2>
    <p class="works__text">The majority of our business is done safely and securely through one of the major postal services (overnight, ground, priority mail). Utilizing insured overnight delivery, you have the option to have your jewelry back to you within a couple days.</p>
    <div class="works__label">Example Scenario:</div>
    <ul class="ticks">
      <li><svg class="tick" width="9" height="9" viewBox="0 0 10 10"><circle cx="5" cy="5" r="4.2" fill="none" stroke="#fff" stroke-width="1"/><path d="M3 5.2l1.5 1.4L7.4 3.6" fill="none" stroke="#fff" stroke-width="1.2"/></svg>You ship your item(s), with instructions for each job.</li>
      <li><svg class="tick" width="9" height="9" viewBox="0 0 10 10"><circle cx="5" cy="5" r="4.2" fill="none" stroke="#fff" stroke-width="1"/><path d="M3 5.2l1.5 1.4L7.4 3.6" fill="none" stroke="#fff" stroke-width="1.2"/></svg>We receive your items and give you a call with any questions or concerns.</li>
      <li><svg class="tick" width="9" height="9" viewBox="0 0 10 10"><circle cx="5" cy="5" r="4.2" fill="none" stroke="#fff" stroke-width="1"/><path d="M3 5.2l1.5 1.4L7.4 3.6" fill="none" stroke="#fff" stroke-width="1.2"/></svg>Our Master Jewelers will provide the quality work.</li>
      <li><svg class="tick" width="9" height="9" viewBox="0 0 10 10"><circle cx="5" cy="5" r="4.2" fill="none" stroke="#fff" stroke-width="1"/><path d="M3 5.2l1.5 1.4L7.4 3.6" fill="none" stroke="#fff" stroke-width="1.2"/></svg>We ship your items back to you via whatever shipping method chosen.</li>
      <li><svg class="tick" width="9" height="9" viewBox="0 0 10 10"><circle cx="5" cy="5" r="4.2" fill="none" stroke="#fff" stroke-width="1"/><path d="M3 5.2l1.5 1.4L7.4 3.6" fill="none" stroke="#fff" stroke-width="1.2"/></svg>You receive the package, inspect the work, and finish the sale.</li>
    </ul>
  </div>

  <div class="gallery" style="top:807px">
    <div class="gem gem--a" role="img" aria-label="Render of a white gold halo engagement ring"></div>
    <div class="gem gem--b" role="img" aria-label="Render of stacked two-tone rings"></div>
    <div class="gem gem--c" role="img" aria-label="Render of two yellow gold cluster rings"></div>
    <div class="gem gem--d" role="img" aria-label="Photo of a rose gold ring set"></div>
  </div>

  <div class="call-bar">Call Us: 1-888-555-0146</div>

  <footer class="sign-off" style="top:966px">
    <div class="sign-off__head">CALL LEM <b>OR</b> GRANT TRAVIS?</div>
    <div class="sign-off__firm">Lem Travis Manufacturing, LLC | <small>12 Heron Court Marlow, LA 70000</small></div>
    <div class="sign-off__contact">Phone: 1-888-555-0146 &nbsp;|&nbsp; Local: 318-555-0172 &nbsp;|&nbsp; E-mail: grant@lemtravismfg.com</div>
  </footer>
</section>

<section class="flyer flyer--back" aria-label="Flyer back">
  <header class="masthead">
    <div class="brand-tag"><span class="brand-tag__dot"></span>LEM TRAVIS</div>
    <div class="masthead__name">
      <div class="masthead__first">LEM TRAVIS</div>
      <div class="masthead__second">MANUFACTURING</div>
      <div class="masthead__tag">TOP QUALITY CRAFTSMANSHIP, FRIENDLY PERSONAL SERVICE</div>
    </div>
  </header>

  <div class="intro">
    <p>Starting with a simple customer's sketch, <b>LEM TRAVIS MANUFACTURING</b> can create any customized piece in yellow gold, white gold, or platinum. Depending on which process best suits your design, we will either hand carve the wax or use <b>CAD/CAM</b> (Computer-Aided Design &amp; Manufacturing). We then cast it and provide you with a beautiful finished product. We can use your stones, your customer's stones, or we can furnish stones for you from our competitively priced inventory.</p>
    <p>We also commonly hand carve and cast waxes for custom fit wedding bands, unique pendants, fashionable earrings, and much more! <b style="font-weight:500">If you can dream it, we can create it.</b></p>
  </div>

  <h2 class="section-title voices-title"><span class="section-title__light">WHAT OTHERS</span><span class="section-title__bold">ARE SAYING?</span></h2>
  <svg class="bubbles" width="110" height="60" viewBox="0 0 110 60" aria-hidden="true">
    <g fill="none" stroke="#0455a3" stroke-width="2.5">
      <rect x="3" y="4" width="42" height="26" rx="3" fill="#fff"/>
      <rect x="9" y="9" width="30" height="16" rx="2"/>
      <path d="M10 30 L8 38 L18 30"/>
      <rect x="58" y="24" width="42" height="26" rx="3" fill="#fff"/>
      <rect x="64" y="29" width="30" height="16" rx="2"/>
      <path d="M64 50 L62 58 L72 50"/>
    </g>
  </svg>

  <div class="quote" style="top:438px">"I have been doing business with Lem Travis Mfg. over 10 years. They are easy to work with &amp; the quality of their work is outstanding. Also, he treats all my jobs large or small with the same quality work. I have total trust &amp; confidence in them."
    <div class="quote__by">Nora Whitfield ~ Hollis Jewelers ~ Ashbury, NC</div></div>

  <div class="quote" style="top:536px">"I just wanted to let you know how much we appreciate your help. Your work is always excellent. The oval ring you just sent us was absolutely beautiful!!"
    <div class="quote__by">Ray &amp; Lena Dobbs ~ Ray's Jewelers ~ Cypress Bend, LA</div></div>

  <div class="quote" style="top:616px">"We have been doing business with Lem Travis Mfg. for many years. We have found them to be very professional. They are real craftsman &amp; very easy to work with. They have completed many specialty &amp; intricate jobs for us, &amp; we have always been pleased with their work. We at Hanley's would be more than happy to recommend them to anyone who would want to use their services!"
    <div class="quote__by">Curtis Hanley ~ Hanley's Fine Jewelry ~ Bayport, AL</div></div>

  <div class="quote" style="top:752px">"We have had the pleasure of working with Lem Travis Mfg. for over 10 years. Their professionalism and work are outstanding. Looking forward to many more years of an excellent working relationship."
    <div class="quote__by">Janet Crowe, Manager ~ Facets &amp; Designs ~ Millbrook, VA</div></div>

  <div class="gallery" style="top:830px;padding:0 56px">
    <div class="gem gem--a" style="width:82px;height:82px" role="img" aria-label="Render of a white gold halo engagement ring"></div>
    <div class="gem gem--b" style="width:82px;height:82px" role="img" aria-label="Render of stacked two-tone rings"></div>
    <div class="gem gem--c" style="width:82px;height:82px" role="img" aria-label="Render of two yellow gold cluster rings"></div>
    <div class="gem gem--d" style="width:82px;height:82px" role="img" aria-label="Photo of a rose gold ring set"></div>
  </div>

  <div class="back-call">Call Us: 1-888-555-0146</div>

  <footer class="back-foot">
    <div class="sign-off" style="top:16px;color:#fff">
      <div class="sign-off__head">CALL LEM OR GRANT TRAVIS?</div>
      <div class="sign-off__firm">Lem Travis Manufacturing, LLC | <small>12 Heron Court Marlow, LA 70000</small></div>
      <div class="sign-off__contact" style="margin-top:12px">Phone: 1-888-555-0146 &nbsp;|&nbsp; Local: 318-555-0172 &nbsp;|&nbsp; E-mail: grant@lemtravismfg.com</div>
    </div>
  </footer>
</section>

</body>
</html>
```